Animated GIF banner for mobile app

We need a GIF Banner designed that alternates between two different ads.

Details are;
Pixel Size (W X H) 300 X 250
Minimum DPI 72dpi
File Size 40kb
File Size (Rich Media) 150kb

Ad 1 Text:
Lost super? More than one super fund? Contact us

Ad 2 Text:
Time to review your home loan? Contact us

Target Market(s)

30-55 year olds

Industry/Entity Type

Financial Service

Font styles to use
Sans Serif

Colors
0555a3
3176b5
85abd2

```html
<!DOCTYPE html>
<html lang="en">
<head>
<meta charset="utf-8">
<title>Banner Preview</title>
<link rel="stylesheet" href="https://fonts.googleapis.com/css2?family=Open+Sans:wght@400;600;800&family=Fira+Sans:wght@500&family=Arimo&display=swap">
<style>
  :root {
    --navy: #0b3f84;
    --brand-blue: #0555a3;
    --mid-blue: #3176b5;
    --light-blue: #85abd2;
    --wall-light: #f7f7f7;
    --wall-dark: #dcdcdc;
    --green-top: #4cb93c;
    --green-bottom: #268a1c;
    --red-top: #c6302d;
    --red-bottom: #8e1512;
    --board-center: #ffffff;
    --board-edge: #dedede;
    --ink: #111111;
  }
  * { box-sizing: border-box; margin: 0; padding: 0; }
  html, body { width: 1200px; height: 1000px; overflow: hidden; }
  body {
    position: relative;
    background: radial-gradient(ellipse at 50% 48%, var(--board-center) 45%, var(--board-edge) 100%);
    font-family: "Open Sans", sans-serif;
  }
  .banner {
    position: absolute;
    top: 413px;
    width: 300px;
    height: 250px;
    border: 1px solid #222;
    overflow: hidden;
    text-align: center;
    color: var(--navy);
  }
  .banner--super { left: 264px; }
  .banner--loan { left: 637px; }
  .wall {
    position: absolute; inset: 0;
    background: radial-gradient(ellipse at 50% 45%, var(--wall-light) 35%, var(--wall-dark) 100%);
  }
  .brand {
    position: absolute; top: 12px; left: 0; right: 0;
    display: flex; justify-content: center; align-items: center; gap: 10px;
    color: var(--brand-blue); font-weight: 400;
  }
  .brand__dot { width: 30px; height: 30px; border-radius: 50%; background: var(--brand-blue); }
  .brand__name { font-size: 21px; line-height: 1; text-align: left; }
  .brand__name small { display: block; font-size: 13px; margin-top: 3px; }
  .headline { position: absolute; left: 0; right: 0; line-height: 1; }
  .headline--lost { top: 92px; font-size: 32px; font-weight: 800; }
  .subline { position: absolute; left: 0; right: 0; top: 134px; font-size: 19px; font-weight: 600; }
  .headline--loan { top: 74px; font-size: 34px; }
  .headline--loan span { display: block; }
  .headline--loan .heavy { font-weight: 800; }
  .headline--loan .light { font-weight: 400; font-size: 33px; }
  .cta {
    position: absolute; left: 60px; width: 178px; height: 38px;
    border-radius: 3px;
    font-family: "Fira Sans", sans-serif; font-weight: 500; font-size: 19px;
    color: #fff; line-height: 38px;
    box-shadow: 0 1px 2px rgba(0,0,0,.35);
  }
  .cta--green { top: 191px; background: linear-gradient(var(--green-top), var(--green-bottom)); }
  .cta--red { top: 196px; background: linear-gradient(var(--red-top), var(--red-bottom)); }
  .caption {
    position: absolute; top: 748px; left: 0; right: 0; text-align: center;
    font-family: "Arimo", sans-serif; font-size: 28px; color: var(--ink);
  }
</style>
</head>
<body>
  <section class="banner banner--super">
    <div class="wall" role="img" aria-label="White painted brick wall background"></div>
    <div class="brand"><span class="brand__dot"></span><span class="brand__name">Daniel Hartley<small>Financial Solutions</small></span></div>
    <h1 class="headline headline--lost">LOST SUPER?</h1>
    <p class="subline">More than one super fund?</p>
    <div class="cta cta--green">Contact Us</div>
  </section>

  <section class="banner banner--loan">
    <div class="wall" role="img" aria-label="White painted brick wall background"></div>
    <div class="brand"><span class="brand__dot"></span><span class="brand__name">Daniel Hartley<small>Financial Solutions</small></span></div>
    <h1 class="headline headline--loan">
      <span class="heavy">TIME TO</span>
      <span class="light">REVIEW YOUR</span>
      <span class="heavy">HOME LOAN?</span>
    </h1>
    <div class="cta cta--red">Contact Us</div>
  </section>

  <p class="caption">Gif animation preview attached</p>
</body>
</html>
```